female stress management consultant, doctor, Health & Well-being coach needs a wordpress theme

I am a Stress management consultant, General Practitioner and Health and Well-Being coach who is targeting mainly surgeries/hospitals and corporate business.
I have my own URL drhelgabrunsvik.com and the hosting.
I need a WordPress Website that is easy to maintain and edit to regularly change the content (copy/pictures/action buttons/banners).
I want my website to look professional and elegant for corporate businesses and managers to feel they can trust me and my expertise. At the same time, the website should have a warm and welcoming feel to it. It should feel uplifting and very positive.
I am open to colour suggestions, but please incorporate the following two colours: #F18877 and #D2BB7A. For fonts I prefer grey over black (like #777777).
The website needs to create an impression of "know like and trust".
The website should have a sign-up button for a newsletter, multiple contact buttons over the home page - to write an email to me, contact details top and bottom and the possibility to have a video on the home page top instead of a picture (Best would be that I can change from picture to video to picture in the future without needing a designer). A video that can run in the background with text laid over. A bit like on this website from Tessa Vanrijn: https://www.tessavanrijn.com.
I need 5 pages: Home, About, Services, Contact, free resources. I do NOT need an e-commerce or booking facility as I will neither sell nor let people book through my website. I don't need a blog either.
All the pages need to have a link to my other website (brightpathdaily.co.uk) and it needs to state that the linked website (brightpathdaily) is my website with a blog and for private customers.
Please use the photos I attached if possible. Me with the dogs for the "about" section.

Websites I like: https://www.olgabkr.com, tessavanrijn.com, https://ruthpembly.com (this site is too dark for my liking, but the layout has a simple navigation layout, the important buttons are right up at the side (WorkLattice/social media/CTA), is minimalistic - hence easy to find the important bits).

Target Market(s)

surgeries/doctor offices, hospitals, corporate business

Industry/Entity Type

Health and well-being

Coding

Coded - Design and coding required

Number of Pages Required

5+ page

Font styles to use
Sans Serif

Requirements
Must have
• see project description
Nice to have
• see project description

```html
<!DOCTYPE html>
<html lang="en">
<head>
<meta charset="utf-8">
<title>Dr Helga Brunsvik – Health, Wellbeing &amp; Happiness</title>
<link rel="stylesheet" href="https://fonts.googleapis.com/css2?family=Libre+Baskerville:wght@400;700&family=Montserrat:wght@400;500;600;700&display=swap">
<style>
:root{
  --coral:#F18877;
  --coral-deep:#e9735f;
  --gold:#D2BB7A;
  --grey:#777777;
  --grey-dark:#555555;
  --pink-pale:#fde6e1;
  --cream:#fbf6f1;
  --white:#ffffff;
  --footer:#2b2b2b;
  --footer-line:#444444;
  --serif:'Libre Baskerville', Georgia, serif;
  --sans:'Montserrat', Arial, sans-serif;
}
*{box-sizing:border-box;margin:0;padding:0}
html,body{width:1200px;height:4108px;overflow:hidden}
body{position:relative;background:var(--white);font-family:var(--sans);color:var(--grey);font-size:14px;line-height:1.7}
.abs{position:absolute}
.btn{position:absolute;display:flex;align-items:center;justify-content:center;border-radius:24px;font-family:var(--sans);font-weight:600;font-size:13px;height:40px;text-decoration:none}
.btn-coral{background:var(--coral);color:var(--white)}
.btn-outline{border:1.5px solid var(--coral);color:var(--coral);background:var(--white)}
.heart{position:absolute;width:30px;height:28px}
.section-title{position:absolute;left:0;width:1200px;text-align:center;font-family:var(--serif);font-weight:700;color:var(--grey-dark);text-transform:uppercase}

/* header */
.site-header{position:absolute;left:0;top:0;width:1200px;height:70px;z-index:2}
.brand{position:absolute;left:60px;top:14px;display:flex;flex-direction:column}
.brand-name{font-family:var(--sans);font-weight:600;font-size:17px;color:var(--coral);line-height:1.2}
.brand-tag{font-size:10px;color:var(--grey)}
.main-nav{position:absolute;left:458px;top:22px;display:flex;gap:30px;font-size:12px;font-weight:600;color:var(--grey-dark);letter-spacing:.5px}
.header-cta{left:860px;top:16px;width:110px;height:36px;font-size:12px}
.social{position:absolute;left:1000px;top:27px;display:flex;gap:10px}
.social span{width:14px;height:14px;border:1.5px solid var(--coral);border-radius:50%}

/* hero */
.hero{left:0;top:0;width:1200px;height:560px;background:linear-gradient(100deg,#e8ddcf 0%,#f2d9bb 40%,#eec096 70%,#d9a47a 100%)}
.play{left:574px;top:300px;width:52px;height:52px}
.hero-title{left:0;top:372px;width:1200px;text-align:center;font-family:var(--serif);font-weight:700;font-size:34px;line-height:1.35;color:var(--white);text-transform:uppercase;text-shadow:0 2px 8px rgba(120,70,40,.35)}

/* about */
.about-bg{left:0;top:640px;width:700px;height:420px;background:var(--pink-pale)}
.about-title{left:120px;top:720px;font-family:var(--serif);font-weight:700;font-size:30px;color:var(--grey-dark)}
.about-lead{left:120px;top:775px;width:520px;font-size:14px;color:var(--grey-dark);line-height:1.6}
.about-text{left:120px;top:830px;width:520px;font-size:13px}
.about-text em{font-style:normal;color:var(--coral)}
.about-photo-back{left:705px;top:640px;width:480px;height:430px;background:var(--coral);border-radius:28px;opacity:.25}
.about-photo{left:720px;top:660px;width:440px;height:390px;border-radius:24px;background:linear-gradient(140deg,#9bb07a,#c9b58c 55%,#8a7a5a)}

/* help cards */
.card{position:absolute;top:1260px;width:360px;height:320px;border-radius:26px;color:var(--white);text-align:center;padding:30px 34px}
.card-coaching{left:220px;background:var(--coral)}
.card-talks{left:620px;background:var(--gold)}
.card h3{font-family:var(--serif);font-weight:700;font-size:17px;line-height:1.4;text-transform:uppercase}
.card h4{font-weight:500;font-size:16px;margin:10px 0 10px}
.card p{font-size:12px;line-height:1.65}
.card .info{position:absolute;left:50%;bottom:22px;width:22px;height:22px;margin-left:-11px}

/* revitalise */
.revit-sub{position:absolute;left:0;width:1200px;text-align:center;font-family:var(--sans);font-weight:500;font-size:28px;color:var(--grey-dark);text-transform:uppercase;line-height:1.35}
.circle-big{left:-10px;top:1880px;width:530px;height:450px;border-radius:50%;background:linear-gradient(150deg,#cfd9e2,#e9dccb 60%,#b9a58a);border:6px solid var(--white)}
.circle-small{left:180px;top:2220px;width:400px;height:390px;border-radius:50%;background:linear-gradient(150deg,#d8c7b0,#ecdccb 55%,#a98f73);border:8px solid var(--white)}
.revit-text{left:590px;top:1880px;width:540px;font-size:13px}
.revit-text p{margin-bottom:16px}
.talk-btn{left:400px;top:2672px;width:130px}
.future-btn{left:550px;top:2672px;width:230px}

/* testimonial */
.testimonial{left:0;top:2800px;width:1200px;height:520px;background:linear-gradient(180deg,#f3a08f 0%,#ee8a76 55%,#f09a88 100%)}
.quote-mark{position:absolute;font-family:var(--serif);font-weight:700;font-size:120px;color:var(--gold);line-height:1}
.testi-title{left:0;top:2900px;width:1200px;text-align:center;font-family:var(--serif);font-weight:700;font-size:34px;line-height:1.3;color:var(--white);text-transform:uppercase}
.testi-quote{left:300px;top:3010px;width:600px;text-align:center;font-size:13px;color:var(--white)}
.testi-name{left:0;top:3120px;width:1200px;text-align:center;font-size:14px;color:var(--white);font-weight:600}
.testi-role{left:0;top:3142px;width:1200px;text-align:center;font-size:11px;color:var(--white)}
.dots{left:576px;top:3210px;display:flex;gap:10px}
.dots span{width:8px;height:8px;border-radius:50%;background:rgba(255,255,255,.55)}
.dots span:first-child{background:var(--white)}

/* blog link */
.blog-sub{left:0;top:3462px;width:1200px;text-align:center;font-size:20px;color:var(--coral);font-weight:500}

/* footer */
.site-footer{left:0;top:3608px;width:1200px;height:500px;background:var(--footer);color:#cfcfcf}
.news-title{left:110px;top:3650px;font-family:var(--serif);font-weight:700;font-size:16px;line-height:1.5;color:var(--white);text-transform:uppercase}
.news-input{left:700px;top:3660px;width:380px;height:40px;border:1px solid #777;border-radius:22px;padding:0 20px;font-size:12px;display:flex;align-items:center;color:#aaa}
.news-submit{left:1050px;top:3662px;width:36px;height:36px;border-radius:50%;background:var(--coral)}
.footer-line{left:110px;top:3730px;width:980px;height:1px;background:var(--footer-line)}
.footer-brand{left:110px;top:3770px;width:190px;height:190px;display:flex;flex-direction:column;align-items:center;justify-content:center;text-align:center}
.footer-brand .mark{width:36px;height:36px;border-radius:50%;background:var(--coral);margin-bottom:14px}
.footer-brand .brand-name{font-size:19px}
.footer-brand .brand-tag{color:#bbb;font-size:11px}
.footer-about{left:330px;top:3770px;width:380px;font-size:12px;line-height:1.6}
.footer-about h5{font-size:14px;color:var(--white);font-weight:700;margin-bottom:10px;letter-spacing:.5px}
.footer-about p{margin-bottom:8px}
.footer-col{top:3770px;font-size:12px;line-height:1.9}
.footer-col h5{font-size:13px;color:var(--white);font-weight:700;margin-bottom:6px;letter-spacing:.5px}
.quick{left:780px}
.legal{left:950px}
.copyright{left:0;top:4070px;width:1200px;text-align:center;font-size:11px;color:#999}
</style>
</head>
<body>

<!-- hero -->
<div class="abs hero" role="img" aria-label="Background video still of a laughing woman in a sun hat against a warm sunset sky"></div>

<header class="site-header">
  <div class="brand">
    <span class="brand-name">Dr Helga Brunsvik</span>
    <span class="brand-tag">Create a life you love living</span>
  </div>
  <nav class="main-nav"><span>HOME</span><span>ABOUT</span><span>SERVICES</span><span>CONTACT</span></nav>
  <a class="btn btn-coral header-cta">Get Quote</a>
  <div class="social"><span></span><span></span><span></span></div>
</header>

<svg class="abs play" viewBox="0 0 52 52" aria-hidden="true">
  <circle cx="26" cy="26" r="25" fill="rgba(255,255,255,.35)" stroke="#fff" stroke-width="2"/>
  <path d="M21 16 L37 26 L21 36 Z" fill="#fff"/>
</svg>
<h1 class="abs hero-title">Live your best life:<br>Happy &amp; Healthy &amp; Full of Joy!</h1>

<!-- about -->
<section>
  <div class="abs about-bg"></div>
  <svg class="heart" style="left:120px;top:680px" viewBox="0 0 30 28" aria-hidden="true"><path d="M15 27 C5 19 0 14 0 8 A7.5 7.5 0 0 1 15 5 A7.5 7.5 0 0 1 30 8 C30 14 25 19 15 27Z" fill="#F18877"/></svg>
  <h2 class="abs about-title">ABOUT ME</h2>
  <p class="abs about-lead">Unlock the Power of Joy and Well-Being: Discover Simple Steps to Restore Your Happiness and Health Today!</p>
  <p class="abs about-text">With <em>over 30 years of being a doctor</em>, I've met countless people facing ongoing health issues and struggles that couldn't be solved easily through conventional medicine. That's why <em>it is so important to embrace a holistic approach</em> in our quest for balance, shifting from discomfort to vitality and contentment.</p>
  <a class="btn btn-coral" style="left:120px;top:968px;width:120px">Learn More</a>
  <div class="abs about-photo-back"></div>
  <div class="abs about-photo" role="img" aria-label="Photo of the doctor sitting outdoors with her two dogs"></div>
</section>

<!-- how I help -->
<section>
  <svg class="heart" style="left:585px;top:1140px" viewBox="0 0 30 28" aria-hidden="true"><path d="M15 27 C5 19 0 14 0 8 A7.5 7.5 0 0 1 15 5 A7.5 7.5 0 0 1 30 8 C30 14 25 19 15 27Z" fill="#F18877"/></svg>
  <h2 class="section-title" style="top:1180px;font-size:30px">How I Help</h2>
  <div class="card card-coaching">
    <h3>1:1 Coaching online or<br>in person</h3>
    <h4>Get personal support</h4>
    <p>Let's embark on a journey together to create a life you love living. As your trusted health coach and experienced doctor, I'll provide comprehensive support and guidance. Together, we'll overcome obstacles, unlock your potential, and design a roadmap to health and happiness.</p>
    <svg class="info" viewBox="0 0 22 22" aria-hidden="true"><circle cx="11" cy="11" r="10" fill="#fff"/><rect x="10" y="9" width="2" height="7" fill="#F18877"/><circle cx="11" cy="6.5" r="1.3" fill="#F18877"/></svg>
  </div>
  <div class="card card-talks">
    <h3>Talks &amp; Workshops</h3>
    <h4 style="margin-top:34px">Get motivated &amp; into action</h4>
    <p>My health and well-being talks and workshops are transformative. They provide knowledge, support and motivation for positive change. Engaging in these discussions connects you to a community, empowers you with insight, and promotes self-awareness. Get ready for a brighter, healthier life!</p>
    <svg class="info" viewBox="0 0 22 22" aria-hidden="true"><circle cx="11" cy="11" r="10" fill="#fff"/><rect x="10" y="9" width="2" height="7" fill="#D2BB7A"/><circle cx="11" cy="6.5" r="1.3" fill="#D2BB7A"/></svg>
  </div>
</section>

<!-- revitalise -->
<section>
  <svg class="heart" style="left:585px;top:1650px" viewBox="0 0 30 28" aria-hidden="true"><path d="M15 27 C5 19 0 14 0 8 A7.5 7.5 0 0 1 15 5 A7.5 7.5 0 0 1 30 8 C30 14 25 19 15 27Z" fill="#F18877"/></svg>
  <h2 class="section-title" style="top:1692px;font-size:32px">Revitalise your life with ease:</h2>
  <p class="revit-sub" style="top:1740px">Master the art of self-care in simple,<br>yet powerful ways!</p>
  <div class="abs circle-big" role="img" aria-label="Photo of a smiling older couple embracing outdoors"></div>
  <div class="abs circle-small" role="img" aria-label="Portrait photo of the doctor smiling"></div>
  <div class="abs revit-text">
    <p>Feeling exhausted, overwhelmed, and constantly drained of energy? It's time to break free from the burdens that weigh you down. Have you experienced unexplained irritability, tearfulness, or a persistent feeling of being down? You know deep down that this isn't the real you. It's time to reclaim your vitality and joy.</p>
    <p>If you're tired of seeking answers in conventional medicine without success, you're not alone. Many people face similar struggles. But the solution often lies in taking a holistic approach, considering all aspects of your well-being and the factors that have led to your current state. Let's uncover the secrets to a life filled with joy and vitality.</p>
    <p>Imagine a life where daily activities become transformative tools for improving your physical and mental health. Through the power of timeless wisdom and modern research, you can achieve your goals and create a life that brings you true happiness. I'm here to guide you on this transformative journey.</p>
    <p>Are you ready to take control of your well-being and unlock the secrets to a fulfilling life? It only takes a spark of curiosity, a commitment to change, and the determination to embrace a new path. Get ready to embark on your transformational journey.</p>
  </div>
  <a class="btn btn-coral talk-btn">Let's Talk</a>
  <a class="btn btn-outline future-btn">Start Your Exciting Future</a>
</section>

<!-- testimonial -->
<section>
  <div class="abs testimonial" role="img" aria-label="Soft coral-toned background photo of a bright outdoor scene"></div>
  <span class="quote-mark" style="left:150px;top:2960px">&ldquo;</span>
  <span class="quote-mark" style="left:990px;top:2960px">&rdquo;</span>
  <h2 class="abs testi-title">I feel more positive and stopped<br>procrastination.</h2>
  <p class="abs testi-quote">Working with Dr Helga Brunsvik has made me way more positive and helped me to stop procrastination. I feel more connected to my true self – the inner fish has finally stopped thrashing around. I feel very relaxed and grounded. Thank you!</p>
  <p class="abs testi-name">Nora Halvik</p>
  <p class="abs testi-role">Counsellor, Psychotherapist, Team Coach, Retreat Host</p>
  <div class="abs dots"><span></span><span></span><span></span></div>
</section>

<!-- blog link -->
<section>
  <svg class="heart" style="left:585px;top:3355px" viewBox="0 0 30 28" aria-hidden="true"><path d="M15 27 C5 19 0 14 0 8 A7.5 7.5 0 0 1 15 5 A7.5 7.5 0 0 1 30 8 C30 14 25 19 15 27Z" fill="#F18877"/></svg>
  <h2 class="section-title" style="top:3400px;font-size:30px">For blog and private customers</h2>
  <p class="abs blog-sub">Heal yourself now!</p>
  <a class="btn btn-coral" style="left:540px;top:3512px;width:120px">Get Started</a>
</section>

<!-- footer -->
<footer>
  <div class="abs site-footer"></div>
  <h3 class="abs news-title">Get regular inspiration for<br>health, wellbeing &amp; happiness</h3>
  <div class="abs news-input">Email ID</div>
  <svg class="abs news-submit" viewBox="0 0 36 36" aria-hidden="true"><circle cx="18" cy="18" r="18" fill="#F18877"/><path d="M11 18 H24 M19 13 L24 18 L19 23" stroke="#fff" stroke-width="2" fill="none"/></svg>
  <div class="abs footer-line"></div>
  <div class="abs footer-brand">
    <span class="mark"></span>
    <span class="brand-name">Dr Helga Brunsvik</span>
    <span class="brand-tag">Create a life you love living</span>
  </div>
  <div class="abs footer-about">
    <h5>DR HELGA BRUNSVIK, MD, PHD</h5>
    <p>"Spend some time with yourself every day."<br>Mira Solen</p>
    <p>The time that you invest in yourself, your health and your happiness will be the best investment you can make. You can't buy happiness, but you can create it.</p>
  </div>
  <div class="abs footer-col quick">
    <h5>QUICK LINKS</h5>
    About<br>Contact<br>Coaching<br>Free Resources
  </div>
  <div class="abs footer-col legal">
    <h5>LEGAL</h5>
    Privacy Policy<br>Disclaimer
  </div>
  <p class="abs copyright">2023 Dr. Helga Brunsvik. All Rights Reserved.</p>
</footer>

</body>
</html>
```